Talbrin Business Cards

Front and back. Simon Kavelle MBA is the CEO of Talbrin Homes. Black white and grays. Logo and cool design.

Target Market(s)

Professional lenders and investors

Industry/Entity Type

Real estate developer. NO HOUSES OR ROOFS

Contact Information for Business Card

Logo, name and unique design. Front and back. Simon Kavelle MBA is the CEO of Talbrin Homes. Black white and grays. Logo and cool design.

Font styles to use
Sans Serif

Colors

Designer to choose only greyscale colors for use in the design.

Requirements
Must have
• Cool look. Not the same card I could design.
Nice to have
• Something memorable
Should not have
• Basic

```html
<!DOCTYPE html>
<html lang="en">
<head>
<meta charset="utf-8">
<title>Talbrin Homes – Business Cards</title>
<link href="https://fonts.googleapis.com/css2?family=Montserrat:wght@300;400;600;700;800&display=swap" rel="stylesheet">
<style>
  :root {
    --stage: #2b2b2b;
    --card-black: #121113;
    --ink-white: #f4f4f4;
    --gray-1: #2e2e30;
    --gray-2: #4a4a4c;
    --gray-3: #6e6e70;
    --gray-4: #9a9a9c;
    --gray-5: #d6d6d8;
    --watermark: #3b3a3c;
  }
  * { margin: 0; padding: 0; box-sizing: border-box; }
  html, body { width: 1200px; height: 900px; overflow: hidden; }
  body {
    background: var(--stage);
    font-family: "Montserrat", sans-serif;
    position: relative;
  }
  .card {
    position: absolute;
    left: 240px;
    width: 720px;
    height: 400px;
    background: var(--card-black);
    overflow: hidden;
    box-shadow: 0 10px 30px rgba(0,0,0,.45);
  }
  .card--pattern { top: 40px; }
  .card--contact { top: 460px; }

  /* Stacked name pattern */
  .stack-word {
    position: absolute;
    left: -14px;
    font-weight: 800;
    font-size: 178px;
    line-height: 1;
    letter-spacing: -6px;
    white-space: nowrap;
  }
  .stack-word--1 { top: -70px;  color: var(--gray-1); }
  .stack-word--2 { top: -10px;  color: var(--gray-2); }
  .stack-word--3 { top: 50px;   color: var(--gray-3); }
  .stack-word--4 { top: 110px;  color: var(--gray-4); }
  .stack-word--5 { top: 170px;  color: var(--gray-5); }

  /* Contact side */
  .brand {
    position: absolute;
    top: 44px;
    right: 50px;
    text-align: center;
    color: var(--ink-white);
  }
  .brand__name {
    font-weight: 800;
    font-size: 44px;
    letter-spacing: -1.5px;
    line-height: 1;
  }
  .brand__sub {
    font-weight: 400;
    font-size: 9px;
    letter-spacing: 7px;
    margin-top: 2px;
    padding-left: 40px;
  }
  .person {
    position: absolute;
    left: 60px;
    top: 128px;
    color: var(--ink-white);
  }
  .person__name {
    font-weight: 700;
    font-size: 17px;
    letter-spacing: .5px;
  }
  .person__degree { font-weight: 300; }
  .person__title {
    font-weight: 600;
    font-size: 12px;
    margin-top: 6px;
  }
  .person__rule {
    width: 40px;
    height: 3px;
    background: var(--ink-white);
    margin: 14px 0 12px;
  }
  .contact-line {
    font-weight: 400;
    font-size: 14px;
    line-height: 1.4;
    letter-spacing: .3px;
  }
  .watermark {
    position: absolute;
    left: 30px;
    bottom: -40px;
    font-weight: 800;
    font-size: 220px;
    letter-spacing: -8px;
    line-height: 1;
    color: var(--watermark);
    white-space: nowrap;
  }
</style>
</head>
<body>
  <section class="card card--pattern" aria-label="Card front">
    <div class="stack-word stack-word--1">Talbrin</div>
    <div class="stack-word stack-word--2">Talbrin</div>
    <div class="stack-word stack-word--3">Talbrin</div>
    <div class="stack-word stack-word--4">Talbrin</div>
    <div class="stack-word stack-word--5">Talbrin</div>
  </section>

  <section class="card card--contact" aria-label="Card back">
    <div class="watermark">Talbrin</div>
    <div class="brand">
      <div class="brand__name">Talbrin</div>
      <div class="brand__sub">HOMES</div>
    </div>
    <div class="person">
      <div class="person__name">SIMON KAVELLE <span class="person__degree">MBA</span></div>
      <div class="person__title">CEO</div>
      <div class="person__rule"></div>
      <div class="contact-line">P 5555 555 555</div>
      <div class="contact-line">E simon@talbrinhomes.com</div>
    </div>
  </section>
</body>
</html>
```